I need the following on my business card:
- Name: Dana Whitcomb
- License # 0M93216
- Title: Producer
- Phone: (555) 017-3904
- Email: Dana@CorbelInsuranceServices.com

- Company: Corbel Insurance Services
- Address: 27408 Larkmoor Ave Suite 610, Brookvale, NV 90217
- Website: www.CorbelInsuranceServices.com

Also add our slogan on the card: "Steady Cover, Every Season"

```html
<!DOCTYPE html>
<html lang="en">
<head>
<meta charset="utf-8">
<title>Corbel Insurance Services – Business Card</title>
<link rel="stylesheet" href="https://fonts.googleapis.com/css2?family=Jost:wght@400;500;700&display=swap">
<style>
  :root {
    --navy: #1d2470;
    --green: #0f8a3a;
    --ink: #2b2f3a;
    --paper: #f7f7f5;
    --rule: #8f93b8;
    --backdrop: #dfe6e2;
    --back-center: #16a14a;
    --back-edge: #0f3e66;
    --white: #ffffff;
  }
  * { box-sizing: border-box; margin: 0; padding: 0; }
  html, body {
    width: 1200px; height: 900px; overflow: hidden;
    background: var(--backdrop);
    font-family: "Jost", sans-serif;
  }
  .canvas {
    position: relative; width: 1200px; height: 900px;
    display: flex; flex-direction: column; align-items: center; justify-content: center; gap: 40px;
  }
  .card {
    position: relative; width: 630px; height: 360px;
    border-radius: 4px; overflow: hidden;
    box-shadow: 0 10px 30px rgba(20, 50, 40, 0.18);
  }

  /* Front */
  .card-front { background: var(--paper); color: var(--ink); }
  .brand {
    position: absolute; top: 44px; right: 40px;
    color: var(--navy); font-weight: 700; line-height: 1;
    display: flex; align-items: center; gap: 12px;
  }
  .brand-mark { width: 20px; height: 20px; background: var(--green); flex: none; }
  .brand-name { font-size: 30px; letter-spacing: 0.5px; white-space: nowrap; }
  .divider {
    position: absolute; top: 122px; left: 34px; right: 34px;
    height: 1px; background: var(--rule);
  }
  .person { position: absolute; top: 146px; left: 40px; }
  .person-name {
    color: var(--navy); font-weight: 700; font-size: 21px; line-height: 1.2;
    text-transform: uppercase; letter-spacing: 0.3px;
  }
  .person-title { font-size: 15px; color: var(--ink); margin-top: 2px; }
  .contacts { list-style: none; margin-top: 14px; }
  .contacts li {
    display: flex; align-items: center; gap: 9px;
    font-size: 14.5px; line-height: 1.55; color: var(--ink); white-space: nowrap;
  }
  .contacts svg { width: 15px; height: 15px; flex: none; }
  .license { color: var(--green); font-size: 15px; margin-top: 10px; font-weight: 500; }

  .office {
    position: absolute; top: 146px; right: 52px; text-align: right;
    font-size: 15px; line-height: 1.45; font-style: normal; white-space: nowrap;
  }
  .office-name { color: var(--green); font-weight: 500; }
  .office-address { color: var(--ink); }

  .band-green {
    position: absolute; left: 0; right: 0; bottom: 0; height: 16px;
    background: var(--green);
  }
  .band-navy {
    position: absolute; right: 0; top: 150px; bottom: 0; width: 22px;
    background: var(--navy);
  }
  .slogan {
    position: absolute; right: 0; bottom: 0; width: 260px; height: 44px;
    background: var(--navy); color: var(--white);
    border-top-left-radius: 22px;
    display: flex; align-items: center; justify-content: center;
    font-size: 14.5px; font-weight: 500; white-space: nowrap;
  }

  /* Back */
  .card-back {
    background: radial-gradient(ellipse at 50% 52%, var(--back-center) 0%, #0e7a4a 35%, var(--back-edge) 85%);
    display: flex; align-items: center; justify-content: center;
  }
  .card-back .brand { position: static; color: var(--white); }
  .card-back .brand-mark { background: var(--white); }
  .card-back .brand-name { font-size: 38px; }
</style>
</head>
<body>
<main class="canvas">

  <section class="card card-front" aria-label="Business card front">
    <div class="brand">
      <span class="brand-mark"></span>
      <span class="brand-name">Corbel Insurance Services</span>
    </div>
    <div class="divider"></div>

    <div class="person">
      <h1 class="person-name">Dana Whitcomb</h1>
      <p class="person-title">Producer</p>
      <ul class="contacts">
        <li>
          <svg viewBox="0 0 16 16" aria-hidden="true"><circle cx="8" cy="8" r="8" fill="#0f8a3a"/><path d="M5.2 4.2l1.5-.3.8 2-1 .7a5 5 0 0 0 2.9 2.9l.7-1 2 .8-.3 1.5c-.2.4-.6.6-1 .6A7.2 7.2 0 0 1 4.6 5.2c0-.4.2-.8.6-1z" fill="#fff"/></svg>
          (555) 017-3904
        </li>
        <li>
          <svg viewBox="0 0 16 16" aria-hidden="true"><rect x="1" y="3" width="14" height="10" rx="1" fill="#0f8a3a"/><path d="M1.5 3.8L8 8.8l6.5-5" fill="none" stroke="#fff" stroke-width="1.3"/></svg>
          Dana@CorbelInsuranceServices.com
        </li>
        <li>
          <svg viewBox="0 0 16 16" aria-hidden="true"><circle cx="8" cy="8" r="8" fill="#0f8a3a"/><g fill="none" stroke="#fff" stroke-width="1"><circle cx="8" cy="8" r="5.5"/><ellipse cx="8" cy="8" rx="2.4" ry="5.5"/><path d="M2.5 8h11M3.4 5h9.2M3.4 11h9.2"/></g></svg>
          www.CorbelInsuranceServices.com
        </li>
      </ul>
      <p class="license">License # 0M93216</p>
    </div>

    <address class="office">
      <div class="office-name">Corbel Insurance Services</div>
      <div class="office-address">27408 Larkmoor Ave Suite 610</div>
      <div class="office-address">Brookvale, NV 90217</div>
    </address>

    <div class="band-green"></div>
    <div class="band-navy"></div>
    <div class="slogan">Steady Cover, Every Season</div>
  </section>

  <section class="card card-back" aria-label="Business card back">
    <div class="brand">
      <span class="brand-mark"></span>
      <span class="brand-name">Corbel Insurance Services</span>
    </div>
  </section>

</main>
</body>
</html>
```